An advertising banner 8ft by 4ft

The advertising banner is going on a building to advertise my company's products and services,we install burglar alarms and CCTV systems, please check out our website for the company logo www.corvellan.co.uk and a general theme of what we do.

We are big on control your alarm and CCTV with your smartphone so my be a phone in hand will be good.

I have been established since 1982

Target Market(s)

Home Security, CCTV and burglar alarms

Industry/Entity Type

Security Service

Colors
9bcb3c

Requirements
Must have
• Pictures of CCTV and alarms system our telephone number 0151 637 2184 and our website www.corvellan.co.uk
• Our Company name: Corvellan Security Systems Ltd
• Our Address: Unit 7 Ashgrove Business Park, Pellinor Road, Widnes WA8 3KP
Nice to have
• Check out the following website to have a look at the produces we use (these are our suppliers) https://www.tavelix.co.uk/
• Our building its on the website

```html
<!DOCTYPE html>
<html lang="en">
<head>
<meta charset="utf-8">
<title>Corvellan Security Systems Ltd – Banner</title>
<link rel="stylesheet" href="https://fonts.googleapis.com/css2?family=Bebas+Neue&family=Nunito:wght@700;800&family=Roboto:wght@700;900&display=swap">
<style>
  :root {
    --green: #9bcb3c;
    --charcoal: #555656;
    --ink: #4a4d4c;
    --paper: #ffffff;
    --backdrop: #ececec;
  }
  * { margin: 0; padding: 0; box-sizing: border-box; }
  html, body { width: 1200px; height: 1200px; overflow: hidden; background: var(--backdrop); }
  .banner {
    position: absolute; left: 190px; top: 19px;
    width: 820px; height: 1162px;
    background: var(--paper); overflow: hidden;
  }
  .top-stripe { position: absolute; left: 0; top: 0; width: 820px; height: 50px; }
  .brand {
    position: absolute; left: 0; width: 100%; text-align: center;
    font-family: "Nunito", sans-serif; font-weight: 800; color: var(--ink);
  }
  .brand-name { top: 76px; font-size: 66px; line-height: 1; letter-spacing: 1px; }
  .brand-sub { top: 180px; font-size: 33px; font-weight: 700; line-height: 1; }
  .product-circle {
    position: absolute; top: 244px; width: 220px; height: 220px;
    border-radius: 50%; border: 6px solid var(--charcoal);
  }
  .product-circle.camera { left: 58px; background: radial-gradient(circle at 40% 55%, #3a3a3a 0 18%, #d9d9d9 40%, #f7f7f7 70%); }
  .product-circle.keypad { left: 300px; background: radial-gradient(circle at 50% 45%, #b9d8a0 0 15%, #e8ecef 40%, #f4f0ec 75%); }
  .product-circle.app { left: 543px; background: radial-gradient(circle at 45% 40%, #bfc3c6 0 20%, #e6e8ea 50%, #fafafa 80%); }
  .services-bar {
    position: absolute; left: 3px; top: 480px; width: 817px; height: 42px;
    background: var(--charcoal); color: #fff; text-align: center;
    font-family: "Bebas Neue", sans-serif; font-size: 38px; line-height: 44px;
  }
  .service {
    position: absolute; display: flex; align-items: center; gap: 8px;
    font-family: "Bebas Neue", sans-serif; font-size: 51px; line-height: 1;
    color: var(--ink); white-space: nowrap;
  }
  .service svg { width: 42px; height: 42px; flex: none; margin-top: -4px; }
  .service.domestic { left: 38px; top: 539px; }
  .service.access { left: 455px; top: 539px; }
  .service.commercial { left: 38px; top: 615px; }
  .service.cctv { left: 455px; top: 615px; }
  .divider { position: absolute; left: 0; top: 676px; width: 820px; height: 1px; background: var(--green); }
  .phone-in-hand {
    position: absolute; left: 30px; top: 689px; width: 282px; height: 358px;
    background: linear-gradient(160deg, #f4f4f4 0%, #e9d4c6 55%, #dcb9a4 100%);
    border-radius: 40px 40px 0 0;
  }
  .contact-head {
    position: absolute; left: 348px; top: 787px; width: 440px; height: 35px;
    background: var(--green); color: #fff; text-align: center;
    font-family: "Roboto", sans-serif; font-weight: 700; font-size: 29px; line-height: 36px;
  }
  .contact-line {
    position: absolute; left: 348px;
    font-family: "Roboto", sans-serif; font-weight: 700; color: var(--charcoal);
    font-size: 27px; line-height: 1; white-space: nowrap;
  }
  .contact-phone { top: 842px; font-size: 29px; letter-spacing: 1px; }
  .contact-addr1 { top: 879px; }
  .contact-addr2 { top: 919px; }
  .web-band {
    position: absolute; left: 0; top: 1047px; width: 456px; height: 91px;
    background: var(--green); color: #fff;
    font-family: "Roboto", sans-serif; font-weight: 700; font-size: 27px;
    line-height: 91px; padding-left: 84px;
  }
  .edge-band { position: absolute; left: 748px; top: 1047px; width: 72px; height: 91px; background: var(--green); }
  .mobile-tag { position: absolute; left: 470px; top: 1042px; width: 272px; color: var(--ink); }
  .mobile-tag .small { display: block; font-family: "Bebas Neue", sans-serif; font-size: 58px; line-height: 48px; }
  .mobile-tag .large { display: block; font-family: "Roboto", sans-serif; font-weight: 900; font-size: 68px; line-height: 52px; letter-spacing: 2px; }
  .base-band { position: absolute; left: 0; top: 1151px; width: 820px; height: 11px; background: var(--charcoal); }
</style>
</head>
<body>
<main class="banner">
  <svg class="top-stripe" viewBox="0 0 820 50" aria-hidden="true">
    <polygon points="0,0 820,0 820,2 0,45" fill="var(--green)"/>
    <polygon points="410,25 820,2 820,50" fill="var(--charcoal)"/>
  </svg>

  <h1 class="brand brand-name">Corvellan</h1>
  <p class="brand brand-sub">Security Systems Ltd</p>

  <div class="product-circle camera" role="img" aria-label="Photo of a white bullet CCTV camera"></div>
  <div class="product-circle keypad" role="img" aria-label="Photo of a finger pressing an alarm keypad"></div>
  <div class="product-circle app" role="img" aria-label="Photo of a CCTV camera beside a smartphone showing camera views"></div>

  <div class="services-bar">OUR SERVICES</div>

  <div class="service domestic"><svg viewBox="0 0 44 44"><circle cx="22" cy="22" r="22" fill="var(--green)"/><path d="M12 23l7 7 13-14" fill="none" stroke="#fff" stroke-width="5" stroke-linecap="round" stroke-linejoin="round"/></svg>DOMESTIC ALARMS</div>
  <div class="service access"><svg viewBox="0 0 44 44"><circle cx="22" cy="22" r="22" fill="var(--green)"/><path d="M12 23l7 7 13-14" fill="none" stroke="#fff" stroke-width="5" stroke-linecap="round" stroke-linejoin="round"/></svg>ACCESS CONTROL</div>
  <div class="service commercial"><svg viewBox="0 0 44 44"><circle cx="22" cy="22" r="22" fill="var(--green)"/><path d="M12 23l7 7 13-14" fill="none" stroke="#fff" stroke-width="5" stroke-linecap="round" stroke-linejoin="round"/></svg>COMMERCIAL ALARMS</div>
  <div class="service cctv"><svg viewBox="0 0 44 44"><circle cx="22" cy="22" r="22" fill="var(--green)"/><path d="M12 23l7 7 13-14" fill="none" stroke="#fff" stroke-width="5" stroke-linecap="round" stroke-linejoin="round"/></svg>CCTV SYSTEMS</div>

  <div class="divider"></div>

  <div class="phone-in-hand" role="img" aria-label="Photo of a hand holding a smartphone showing live CCTV preview"></div>

  <div class="contact-head">CONTACT US:</div>
  <p class="contact-line contact-phone">0151 637 2184</p>
  <p class="contact-line contact-addr1">Unit 7 Ashgrove Business Park</p>
  <p class="contact-line contact-addr2">Pellinor Road, Widnes WA8 3KP</p>

  <div class="web-band">www.corvellan.co.uk</div>
  <div class="edge-band"></div>
  <p class="mobile-tag"><span class="small">CCTV ON YOUR</span><span class="large">MOBILE</span></p>

  <div class="base-band"></div>
</main>
</body>
</html>
```